New modern business card design

To design a brand new business card that's clean & modern in terms of layout.
I have attached our company logo and also basic information regarding what is needed on the card that also needs to be editable.

Target Market(s)

motor trade

Contact Information for Business Card

logo, name, title, tel, mob, email, address, www, all information is in the word.doc file

Requirements
Must have
• white background
Nice to have
• Nice clean font

```html
<!DOCTYPE html>
<html lang="en">
<head>
<meta charset="utf-8">
<title>Boltline Ltd – Business Card</title>
<link rel="stylesheet" href="https://fonts.googleapis.com/css2?family=Roboto:wght@400;700&display=swap">
<style>
  :root {
    --backdrop: #e9e7e3;
    --card: #ffffff;
    --brand-blue: #2f7fc4;
    --steel-grey: #9a9ca0;
    --text-dark: #4a4a4a;
    --shadow: rgba(0, 0, 0, 0.18);
  }
  html, body {
    margin: 0;
    width: 1200px;
    height: 911px;
    overflow: hidden;
    background: var(--backdrop);
    font-family: "Roboto", Arial, sans-serif;
  }
  .stage {
    position: relative;
    width: 1200px;
    height: 911px;
  }
  .card {
    position: absolute;
    width: 560px;
    height: 320px;
    background: var(--card);
    box-shadow: 0 6px 18px var(--shadow);
    box-sizing: border-box;
  }
  .card--front { left: 80px; top: 110px; }
  .card--back  { left: 560px; top: 480px; }

  .front-brand {
    position: absolute;
    top: 34px;
    right: 36px;
    color: var(--brand-blue);
    font-weight: 700;
    font-size: 54px;
    letter-spacing: 1px;
    line-height: 1;
  }

  .contact-block {
    position: absolute;
    left: 40px;
    bottom: 30px;
  }
  .person-name {
    margin: 0;
    color: var(--brand-blue);
    font-weight: 700;
    font-size: 19px;
    text-transform: uppercase;
  }
  .person-title {
    margin: 2px 0 12px;
    color: var(--steel-grey);
    font-weight: 400;
    font-size: 13px;
    text-transform: uppercase;
    letter-spacing: 0.5px;
  }
  .address {
    margin: 0 0 10px;
    font-style: normal;
    color: var(--text-dark);
    font-size: 13px;
    line-height: 1.35;
  }
  .contact-list {
    list-style: none;
    margin: 0;
    padding: 0;
    color: var(--text-dark);
    font-size: 13px;
    line-height: 1.5;
  }
  .contact-list li {
    display: flex;
    align-items: center;
    gap: 8px;
  }
  .contact-icon {
    width: 12px;
    height: 12px;
    flex: none;
  }

  .back-brand {
    position: absolute;
    inset: 0;
    display: flex;
    align-items: center;
    justify-content: center;
    gap: 14px;
  }
  .back-brand__mark {
    width: 22px;
    height: 22px;
    background: var(--brand-blue);
  }
  .back-brand__name {
    color: var(--brand-blue);
    font-weight: 700;
    font-size: 36px;
    letter-spacing: 2px;
  }
</style>
</head>
<body>
<main class="stage">
  <section class="card card--front" aria-label="Business card front">
    <div class="front-brand">BOLTLINE</div>
    <div class="contact-block">
      <h1 class="person-name">Daniel Mercer</h1>
      <h2 class="person-title">General Manager</h2>
      <address class="address">
        Kestrel Road<br>
        Dunmore, Northfield<br>
        NF4 2LP
      </address>
      <ul class="contact-list">
        <li>
          <svg class="contact-icon" viewBox="0 0 12 12" aria-hidden="true"><path d="M2.5 1 L4.5 1 L5 3.5 L3.8 4.4 Q5 7 7.6 8.2 L8.5 7 L11 7.5 L11 9.5 Q10.5 11 9 11 Q1 10 1 2.5 Q1 1 2.5 1 Z" fill="var(--brand-blue)"/></svg>
          0100 555 0142
        </li>
        <li>
          <svg class="contact-icon" viewBox="0 0 12 12" aria-hidden="true"><rect x="3" y="0.5" width="6" height="11" rx="1" fill="none" stroke="var(--brand-blue)" stroke-width="1.3"/><circle cx="6" cy="9.6" r="0.7" fill="var(--brand-blue)"/></svg>
          07700 900 318
        </li>
        <li>
          <svg class="contact-icon" viewBox="0 0 12 12" aria-hidden="true"><rect x="0.5" y="2" width="11" height="8" fill="var(--brand-blue)"/><path d="M0.5 2 L6 6.5 L11.5 2" fill="none" stroke="#fff" stroke-width="1"/></svg>
          dmercer@boltline.co.uk
        </li>
        <li>
          <svg class="contact-icon" viewBox="0 0 12 12" aria-hidden="true"><circle cx="6" cy="6" r="5.5" fill="var(--brand-blue)"/><path d="M0.5 6 H11.5 M6 0.5 Q3 6 6 11.5 M6 0.5 Q9 6 6 11.5" fill="none" stroke="#fff" stroke-width="0.8"/></svg>
          www.boltline.co.uk
        </li>
      </ul>
    </div>
  </section>

  <section class="card card--back" aria-label="Business card back">
    <div class="back-brand">
      <span class="back-brand__mark" aria-hidden="true"></span>
      <span class="back-brand__name">BOLTLINE LTD</span>
    </div>
  </section>
</main>
</body>
</html>
```